Landscaping | Turf | With Future Opportunities

The Meadow Lawn (themeadowlawn-example.com) is looking for a website rebuild.
Please see the brief attached.

The Meadow Lawn is the #1 artificial grass instillation company in southern california. They are small, but do great work.

This is a project where you are able to utilize your creative-genius! Imply integrations for review badge (plain shape) reviews, add charts that are lighter grey for the competition, take images from our site and review badge (plain shape) if you're going for a more real-approach.

We are open to creativity!! Competitor sites are not very appealing. We want users to be able to come to our site and have all the information to make an educated decision but also see that we value our online presence.

We are using wordpress so the designer would need to be able to code this into our site upon completion.
Updates

Target Market(s)

Homeowners, 25+ years old, southern california

Industry/Entity Type

Landscaping

Coding

Coded - Design and coding required

Number of Pages Required

3 page

Colors
9bcb3b

Requirements
Must have
• Pages must be responsive (desktop and mobile).
• Must be able to input into wordpress.
• Please use your best judgement to create the following:
• - Form fill so Todd can reach out for estimate times: info needed are first and last name, email, phone number, address and an optional box for memo that lead to his inbox
• - Why we are different (see brief)
• - A link to his review badge (plain shape) page will reviews/ testimonials
• - Photos for his work in his three products: Front yard, backyard, putting greens
• - Certification, reliability, contact info
• - A clear CTA to leave their info with inquiries
• How many pages would this entail? We don't want a ton of unnecessary stuff on site, we dont want it to look cluttered, but we don't want it to be missing info.
• **Please do not rely on the designated pages. Use your best judgement.
• Use current site for color.
Should not have
• Many competitor sites look dated.
• The text and images must be crawl-able on Google so make sure the site reflects this (psd files, not pdf or jpegs)

```html
<!DOCTYPE html>
<html lang="en">
<head>
<meta charset="utf-8">
<title>The Meadow Lawn – Artificial Grass &amp; Putting Greens</title>
<link href="https://fonts.googleapis.com/css2?family=Roboto:wght@400;500;700&family=Open+Sans:wght@400;600&display=swap" rel="stylesheet">
<style>
:root{
  --brand:#4a7a2a;
  --brand-dark:#2f5618;
  --brand-light:#6a9a3e;
  --ink:#1a1a1a;
  --muted:#444;
  --white:#ffffff;
  --band:#0c1a08;
  --footer:#030503;
  --review-red:#d32323;
  --review-orange:#f0a030;
  --star-grey:#c8c8c8;
  --stone:#6e6a62;
  --stone-dark:#4a463f;
}
*{box-sizing:border-box;margin:0;padding:0}
html,body{width:1200px;height:1025px;overflow:hidden;background:var(--white)}
body{font-family:"Roboto",sans-serif;color:var(--ink);position:relative}
a{color:inherit;text-decoration:none}

/* Header */
.site-header{position:absolute;left:0;top:0;width:1200px;height:122px;background:var(--white)}
.brand{position:absolute;left:92px;top:29px;display:flex;align-items:center;gap:10px}
.brand-mark{width:22px;height:22px;background:var(--brand-dark)}
.brand-name{font-weight:700;font-size:27px;color:var(--brand-dark);letter-spacing:.3px}
.license{position:absolute;left:92px;top:72px;width:304px;text-align:center;font-size:15px;letter-spacing:1.3px;color:var(--muted)}
.contact{position:absolute;right:308px;top:29px;text-align:right;line-height:21px}
.contact .hello{font-size:15px}
.contact .hello small{font-size:11px}
.contact .reach{font-size:14px}
.contact .reach .accent{color:var(--brand);font-size:16.5px}
.contact .note{font-size:13.5px}
.cta-button{position:absolute;left:918px;top:29px;width:192px;height:61px;border-radius:3px;
  background:linear-gradient(#6a9a3e,#3f6f22);color:var(--white);font-size:17px;line-height:21px;
  display:flex;align-items:center;justify-content:center;text-align:center;box-shadow:0 2px 5px rgba(0,0,0,.35)}

/* Hero */
.hero{position:absolute;left:0;top:122px;width:1200px;height:551px;overflow:hidden;
  background:
    radial-gradient(ellipse 300px 110px at 790px 60px,rgba(170,200,120,.75) 0%,transparent 75%),
    radial-gradient(ellipse 260px 90px at 1120px 40px,rgba(140,180,90,.6) 0%,transparent 75%),
    radial-gradient(ellipse 200px 260px at 90px 120px,rgba(40,55,30,.9) 0%,transparent 80%),
    radial-gradient(ellipse 380px 120px at 520px 420px,rgba(30,60,15,.55) 0%,transparent 80%),
    linear-gradient(100deg,#27331f 0%,#3d6824 16%,#4f8d2b 42%,#437a25 66%,#2f5c1c 100%)}
.hero-shade{position:absolute;left:0;top:0;width:1200px;height:551px;
  background:linear-gradient(rgba(0,0,0,0) 50%,rgba(0,0,0,.25) 100%)}
.hero-stone{position:absolute;left:-120px;top:412px;width:1440px;height:340px;border-radius:50%;
  background:linear-gradient(#85807a 0%,var(--stone) 25%,var(--stone-dark) 60%)}
.hero-title{position:absolute;left:0;top:264px;width:1200px;text-align:center;color:var(--white);
  font-weight:700;font-size:72px;line-height:76px;text-shadow:0 2px 6px rgba(0,0,0,.4)}
.hero-subtitle{position:absolute;left:0;top:343px;width:1200px;text-align:center;color:var(--white);
  font-weight:500;font-size:44px;line-height:50px;text-shadow:0 2px 6px rgba(0,0,0,.4)}
.hero-tagline{position:absolute;left:0;top:466px;width:1200px;text-align:center;color:#e2e2e2;
  font-weight:500;font-size:33px;line-height:40px;text-shadow:0 2px 4px rgba(0,0,0,.4)}

/* Reviews */
.reviews{position:absolute;left:996px;top:257px;width:204px}
.review{height:57px;margin-bottom:6px;background:var(--white);border-radius:3px 0 0 3px;
  box-shadow:0 1px 4px rgba(0,0,0,.4);position:relative}
.review-thumb{position:absolute;left:7px;top:6px;width:45px;height:45px}
.review-name{position:absolute;left:58px;top:7px;font-size:11px;font-weight:500;color:var(--review-red);white-space:nowrap}
.review-stars{position:absolute;left:58px;top:23px;display:flex;gap:1px}
.star{width:11px;height:11px;background:var(--review-red);color:var(--white);font-size:9px;line-height:11px;text-align:center}
.star.mid{background:var(--review-orange)}
.star.off{background:var(--star-grey)}
.review-count{position:absolute;left:124px;top:24px;font-size:8px;color:#888}
.review-badge{position:absolute;left:60px;top:40px;width:24px;height:8px;border-radius:2px;background:#555}

/* Products */
.products{position:absolute;left:0;top:673px;width:1200px;height:247px;background:var(--band)}
.product{position:absolute;top:-139px;width:280px}
.diamond{position:absolute;left:42px;top:41px;width:196px;height:196px;transform:rotate(45deg);
  border:3px solid var(--white);border-radius:22px;padding:5px;background:var(--band)}
.diamond .photo{width:100%;height:100%;border-radius:16px}
.photo-front{background:
  radial-gradient(ellipse 60px 40px at 30% 20%,#9cc4ea 0%,transparent 90%),
  linear-gradient(135deg,#9cc4ea 0%,#e3d3b4 30%,#c9a27a 45%,#3f6f2a 62%,#5a9a34 80%,#cfd1cc 100%)}
.photo-back{background:
  radial-gradient(ellipse 70px 50px at 70% 55%,#9ccf62 0%,transparent 90%),
  linear-gradient(135deg,#2c4a1e 0%,#4f7f30 30%,#7ab542 55%,#e2e0d8 78%,#f0efe8 100%)}
.photo-green{background:
  radial-gradient(ellipse 80px 60px at 60% 55%,#5fae48 0%,transparent 90%),
  linear-gradient(135deg,#8a7a66 0%,#c8706a 28%,#3f9a3a 45%,#3c8f34 75%,#2d6e26 100%)}
.product-label{position:absolute;left:0;top:294px;width:280px;text-align:center;color:var(--white);font-size:29px;line-height:36px}

/* Footer */
.site-footer{position:absolute;left:0;top:920px;width:1200px;height:105px;background:var(--footer);color:var(--white)}
.footer-nav{position:absolute;left:97px;top:41px;font-family:"Open Sans",sans-serif;font-size:18px}
.footer-nav span{margin:0 14px}
.social{position:absolute;left:459px;top:28px;display:flex;gap:27px}
.social-icon{width:50px;height:50px;border-radius:50%;background:#3d6a1e;border:4px solid #1d3410;
  display:flex;align-items:center;justify-content:center}
.social-icon svg{width:22px;height:22px}
.copyright{position:absolute;right:91px;top:43px;font-family:"Open Sans",sans-serif;font-size:17.5px}
</style>
</head>
<body>

<header class="site-header">
  <div class="brand"><span class="brand-mark"></span><span class="brand-name">The Meadow Lawn</span></div>
  <p class="license">CA License Number: 1000421</p>
  <div class="contact">
    <p class="hello">Hi, I’m Todd! <small>[I’m available for you around the clock.]</small> TO MODIFY</p>
    <p class="reach"><span class="accent">Call (805) 555 0148</span> or email me at <span class="accent">info@themeadowlawn-example.com</span></p>
    <p class="note">Please reach out for a free, no obligation estimate</p>
  </div>
  <a class="cta-button">Receive a Free<br>design consultation</a>
</header>

<section class="hero" role="img" aria-label="Photo of a shaded backyard lawn of artificial grass with a putting green and curved stone edging">
  <div class="hero-shade"></div>
  <div class="hero-stone"></div>
</section>
<h1 class="hero-title">The Meadow Lawn</h1>
<p class="hero-subtitle">Artificial Grass &amp; Putting Greens</p>
<p class="hero-tagline">Professionals in Artificial Grass Installation</p>

<aside class="reviews">
  <div class="review">
    <div class="review-thumb" role="img" aria-label="Customer backyard photo" style="background:linear-gradient(#7a5a3e,#8a6a4a 40%,#4c8a2c 70%)"></div>
    <p class="review-name">Dana R. Oakview</p>
    <div class="review-stars"><span class="star">★</span><span class="star">★</span><span class="star">★</span><span class="star">★</span><span class="star">★</span></div>
    <span class="review-count">7 reviews</span>
    <span class="review-badge"></span>
  </div>
  <div class="review">
    <div class="review-thumb" role="img" aria-label="Customer lawn photo" style="background:linear-gradient(#3f5a2c,#6aa040 50%,#3a6a22)"></div>
    <p class="review-name">Lena T. Hillcrest,</p>
    <div class="review-stars"><span class="star">★</span><span class="star">★</span><span class="star">★</span><span class="star">★</span><span class="star off">★</span></div>
    <span class="review-count">4 reviews</span>
    <span class="review-badge"></span>
  </div>
  <div class="review">
    <div class="review-thumb" role="img" aria-label="Customer front yard photo" style="background:linear-gradient(#8fb3d0,#c8c0a8 45%,#4a7a30 75%)"></div>
    <p class="review-name">Omar K. Fairfield</p>
    <div class="review-stars"><span class="star mid">★</span><span class="star mid">★</span><span class="star mid">★</span><span class="star mid">★</span><span class="star off">★</span></div>
    <span class="review-count">124 reviews</span>
    <span class="review-badge"></span>
  </div>
</aside>

<section class="products">
  <div class="product" style="left:119px">
    <div class="diamond"><div class="photo photo-front" role="img" aria-label="Front yard of a stucco house with an artificial lawn"></div></div>
    <p class="product-label">Front Yard</p>
  </div>
  <div class="product" style="left:449px">
    <div class="diamond"><div class="photo photo-back" role="img" aria-label="Backyard with stone stepping path set in turf"></div></div>
    <p class="product-label">Backyard</p>
  </div>
  <div class="product" style="left:781px">
    <div class="diamond"><div class="photo photo-green" role="img" aria-label="Backyard putting green with flags and brick edging"></div></div>
    <p class="product-label">Putting Greens</p>
  </div>
</section>

<footer class="site-footer">
  <nav class="footer-nav">Home<span>|</span>About<span>|</span>Services</nav>
  <div class="social">
    <a class="social-icon" aria-label="Social profile"><svg viewBox="0 0 24 24" fill="none" stroke="#fff" stroke-width="2.6" stroke-linecap="round" stroke-linejoin="round"><path d="M7 17L17 7M9 7h8v8"/></svg></a>
    <a class="social-icon" aria-label="Social profile"><svg viewBox="0 0 24 24" fill="none" stroke="#fff" stroke-width="2.6" stroke-linecap="round" stroke-linejoin="round"><path d="M7 17L17 7M9 7h8v8"/></svg></a>
    <a class="social-icon" aria-label="Social profile"><svg viewBox="0 0 24 24" fill="none" stroke="#fff" stroke-width="2.6" stroke-linecap="round" stroke-linejoin="round"><path d="M7 17L17 7M9 7h8v8"/></svg></a>
    <a class="social-icon" aria-label="Social profile"><svg viewBox="0 0 24 24" fill="none" stroke="#fff" stroke-width="2.6" stroke-linecap="round" stroke-linejoin="round"><path d="M7 17L17 7M9 7h8v8"/></svg></a>
  </div>
  <p class="copyright">Copyright © 2018&nbsp; All Rights Reserved</p>
</footer>

</body>
</html>
```